Letterhead Design Project

Attached is our new Logo and a copy of our old letter head
Looking to rebrand with our new logo

Reason: I want to show a business card design

Industry/Entity Type

Film Production

Colors

Requirements
Must have
• The information on the old letterhead

```html
<!DOCTYPE html>
<html lang="en">
<head>
<meta charset="utf-8">
<title>Vela International – Stationery Set</title>
<link href="https://fonts.googleapis.com/css2?family=Open+Sans:wght@400;600;700&display=swap" rel="stylesheet">
<style>
  :root{
    --bg:#b3dfeb;
    --paper:#ffffff;
    --brand-blue:#0a6fa8;
    --deep-blue:#0b3f8f;
    --bright-blue:#1bb3e6;
    --orange:#ee7d1a;
    --grey:#c9ccd0;
    --wave:#dff1f8;
    --ink:#4a5560;
  }
  *{box-sizing:border-box;margin:0;padding:0}
  html,body{width:1200px;height:768px;overflow:hidden}
  body{background:var(--bg);font-family:"Open Sans",Arial,sans-serif;color:var(--ink);position:relative}

  .sheet{position:absolute;background:var(--paper);box-shadow:0 8px 24px rgba(20,60,90,.18);overflow:hidden}
  .sheet svg{z-index:0}

  .wordmark{display:flex;align-items:center;gap:6px;color:var(--brand-blue);font-weight:700;letter-spacing:.06em;white-space:nowrap;z-index:2}
  .wordmark .dot{width:8px;height:8px;border-radius:50%;background:var(--orange)}
  .wordmark.light{color:#fff}

  .bar{position:absolute;height:5px;z-index:1}
  .bar.orange{background:var(--orange)}
  .bar.blue{background:var(--brand-blue)}

  /* Letterhead */
  .letterhead{left:640px;top:40px;width:480px;height:680px}
  .letterhead .wordmark{position:absolute;top:66px;left:50%;transform:translateX(-50%);font-size:17px}
  .waves{position:absolute;left:0;bottom:0;width:100%}
  .footer-info{position:absolute;left:24px;right:20px;bottom:26px;z-index:2}
  .tagline{color:var(--brand-blue);font-weight:700;font-size:12px;text-align:right;margin-bottom:8px;padding-right:100px}
  .contacts{display:flex;justify-content:space-between;font-size:7.5px;line-height:1.7}
  .contacts li{list-style:none;display:flex;align-items:center;gap:4px;white-space:nowrap}
  .contacts li::before{content:"";width:5px;height:5px;border-radius:50%;background:var(--orange);flex:none}

  /* Business cards */
  .card{width:340px;height:195px}
  .card-front{left:60px;top:50px;background:linear-gradient(135deg,var(--bright-blue),var(--deep-blue))}
  .card-front .wordmark{position:absolute;top:72px;left:50%;transform:translateX(-50%);font-size:18px}
  .card-front .web{position:absolute;left:16px;bottom:12px;font-size:8px;color:#5d6670;z-index:2}
  .card-back{left:60px;top:272px}
  .card-back .wordmark{position:absolute;top:22px;left:112px;font-size:13px}
  .card-back .contacts{position:absolute;top:52px;left:112px;flex-direction:column;font-size:7.5px;line-height:1.8;z-index:2}
  .person{position:absolute;left:18px;bottom:16px;color:#fff;z-index:2}
  .person .name{font-size:11px;font-weight:700}
  .person .role{font-size:7.5px}
  .card svg{position:absolute;inset:0}

  /* Compliment slip */
  .slip{left:60px;top:494px;width:540px;height:250px}
  .slip .wordmark{position:absolute;top:30px;left:56px;font-size:14px}
  .slip .footer-info{bottom:16px}
  .slip .tagline{font-size:10.5px;padding-right:110px}
  .slip .contacts{font-size:7px}
</style>
</head>
<body>

<section class="sheet card card-front" aria-label="Business card front">
  <svg width="340" height="195" viewBox="0 0 340 195" aria-hidden="true">
    <path d="M0 80 C80 120 170 150 340 160 L340 195 L0 195 Z" fill="#d6d9dc"/>
    <path d="M0 80 C80 120 170 150 340 160 L340 150 C180 140 90 112 0 66 Z" fill="#ffffff" opacity=".85"/>
    <path d="M0 66 C90 112 180 140 340 150 L340 140 C190 128 100 100 0 54 Z" fill="#1bb3e6"/>
  </svg>
  <div class="wordmark light"><span class="dot"></span>VELA INTERNATIONAL</div>
  <p class="web">www.velainternational.com.au</p>
</section>

<section class="sheet card card-back" aria-label="Business card back">
  <svg width="340" height="195" viewBox="0 0 340 195" aria-hidden="true">
    <path d="M0 60 C60 120 160 150 340 150 L340 195 L0 195 Z" fill="#0b3f8f"/>
    <path d="M0 60 C60 120 160 150 340 150 L340 138 C170 138 80 110 10 40 L0 40 Z" fill="#d6d9dc"/>
    <path d="M0 100 C70 150 170 170 340 168 L340 195 L0 195 Z" fill="#0a6fa8"/>
    <path d="M300 0 C318 14 330 28 340 44 L340 0 Z" fill="#0b5aa8"/>
  </svg>
  <div class="wordmark"><span class="dot"></span>VELA INTERNATIONAL</div>
  <ul class="contacts">
    <li>P.O. Box 482 Hillcrest QLD 4118</li>
    <li>P.O. Box 731 Marlow NSW 2195</li>
    <li>0400 555 218 · hello@velaintl.com.au</li>
    <li>ACN 600 482 719 · ABN 51 600 482 719</li>
  </ul>
  <div class="person">
    <p class="name">Example Name</p>
    <p class="role">Designation</p>
  </div>
</section>

<section class="sheet slip" aria-label="Compliment slip">
  <div class="bar orange" style="top:26px;right:0;width:300px"></div>
  <div class="bar blue" style="top:56px;left:0;width:50px"></div>
  <div class="wordmark"><span class="dot"></span>VELA INTERNATIONAL</div>
  <svg class="waves" width="540" height="110" viewBox="0 0 540 110" aria-hidden="true">
    <path d="M0 60 C160 90 340 50 540 20 L540 110 L0 110 Z" fill="var(--wave)"/>
    <path d="M0 90 C200 100 360 70 540 50 L540 110 L0 110 Z" fill="#eef8fc"/>
    <line x1="30" y1="52" x2="180" y2="52" stroke="var(--orange)" stroke-width="1"/>
    <line x1="420" y1="34" x2="520" y2="34" stroke="var(--orange)" stroke-width="1"/>
    <rect x="0" y="104" width="440" height="6" fill="var(--brand-blue)"/>
    <rect x="440" y="104" width="100" height="6" fill="var(--orange)"/>
  </svg>
  <div class="footer-info">
    <p class="tagline">Supply &amp; Management of Infrastructure &amp; Logistics</p>
    <ul class="contacts">
      <li>P.O. Box 482 Hillcrest QLD 4118<br>P.O. Box 731 Marlow NSW 2195</li>
      <li>0400 555 218<br>hello@velaintl.com.au</li>
      <li>ACN 600 482 719<br>ABN 51 600 482 719</li>
      <li>VELA Film Services<br>VELA Tour Management</li>
      <li>VELA Pilot Escorts<br>VELA Driver</li>
    </ul>
  </div>
</section>

<section class="sheet letterhead" aria-label="Letterhead">
  <div class="bar orange" style="top:34px;right:0;width:130px"></div>
  <div class="bar blue" style="top:172px;left:0;width:150px"></div>
  <div class="wordmark"><span class="dot"></span>VELA INTERNATIONAL</div>
  <svg class="waves" width="480" height="150" viewBox="0 0 480 150" aria-hidden="true">
    <path d="M0 90 C150 120 330 70 480 30 L480 150 L0 150 Z" fill="var(--wave)"/>
    <path d="M0 120 C180 135 340 100 480 80 L480 150 L0 150 Z" fill="#eef8fc"/>
    <line x1="20" y1="88" x2="170" y2="88" stroke="var(--orange)" stroke-width="1"/>
    <line x1="370" y1="58" x2="470" y2="58" stroke="var(--orange)" stroke-width="1"/>
    <rect x="0" y="143" width="380" height="7" fill="var(--brand-blue)"/>
    <rect x="380" y="143" width="100" height="7" fill="var(--orange)"/>
  </svg>
  <div class="footer-info">
    <p class="tagline">Supply &amp; Management of Infrastructure &amp; Logistics</p>
    <ul class="contacts">
      <li>P.O. Box 482 Hillcrest QLD 4118<br>P.O. Box 731 Marlow NSW 2195</li>
      <li>0400 555 218<br>hello@velaintl.com.au</li>
      <li>ACN 600 482 719<br>ABN 51 600 482 719</li>
      <li>VELA Film Services<br>VELA Tour Management</li>
      <li>VELA Pilot Escorts<br>VELA Driver</li>
    </ul>
  </div>
</section>

</body>
</html>
```